Design a Flyer for Wedding and Party consultants

I would like to create a Wedding, Bridal, Party flyer which telling a prospective client what we do and what we offer.
The wording in the sample that I upload are wrong. Please use a better English :)

```html
<!DOCTYPE html>
<html lang="en">
<head>
<meta charset="UTF-8">
<title>Evermore Decoration – Wedding Package Flyer</title>
<link href="https://fonts.googleapis.com/css2?family=Courgette&family=Great+Vibes&family=Cinzel:wght@600;700&family=Cormorant+SC:wght@700&display=swap" rel="stylesheet">
<style>
  :root {
    --page-bg: #e9e6e2;
    --paper-light: #fbf6f2;
    --paper-mid: #efe2dc;
    --paper-rose: #e6d2d0;
    --plum: #5e1a4a;
    --plum-deep: #3f0d31;
    --plum-soft: #7a2c62;
    --gold: #e8c04a;
    --gold-deep: #b8862a;
    --photo-warm: #c9a690;
    --photo-cool: #2f3250;
    --cake-tone: #d98a3a;
  }
  * { margin: 0; padding: 0; box-sizing: border-box; }
  html, body {
    width: 1200px;
    height: 880px;
    overflow: hidden;
    background: var(--page-bg);
  }
  .flyer {
    position: absolute;
    left: 300px;
    top: 20px;
    width: 600px;
    height: 840px;
    overflow: hidden;
    background: radial-gradient(ellipse at 50% 45%, var(--paper-light) 0%, var(--paper-mid) 60%, var(--paper-rose) 100%);
    box-shadow: 0 6px 24px rgba(0,0,0,0.18);
  }
  .tagline {
    position: absolute;
    z-index: 3;
    left: 22px;
    top: 40px;
    width: 200px;
    font-family: "Courgette", cursive;
    font-size: 20px;
    line-height: 1.1;
    color: var(--plum-soft);
    text-shadow: 0 0 4px var(--paper-light), 0 0 2px var(--paper-light);
    transform: rotate(-7deg);
    transform-origin: left top;
  }
  .photo-frame {
    position: absolute;
    left: 215px;
    top: 22px;
    width: 280px;
    height: 240px;
    border: 12px solid var(--gold);
    outline: 2px solid var(--gold-deep);
    outline-offset: -2px;
    box-shadow: 0 3px 10px rgba(80,30,50,0.3);
  }
  .couple-photo {
    width: 100%;
    height: 100%;
    background: linear-gradient(100deg, var(--photo-warm) 0%, #b9928a 40%, var(--photo-cool) 75%);
  }
  .cake-art {
    position: absolute;
    left: 80px;
    top: 128px;
    width: 120px;
    height: 130px;
    border-radius: 8px;
    background: linear-gradient(180deg, #e8a552 0%, var(--cake-tone) 60%, #b9412e 100%);
  }
  .services-note {
    position: absolute;
    z-index: 3;
    left: 352px;
    top: 172px;
    width: 128px;
    font-family: "Courgette", cursive;
    font-size: 11px;
    line-height: 1.3;
    color: #ffffff;
    text-shadow: 0 1px 2px rgba(20,5,20,0.9);
  }
  .brand-plaque {
    position: absolute;
    left: 80px;
    top: 274px;
    width: 440px;
    height: 100px;
    border-radius: 6px;
    background: linear-gradient(90deg, var(--plum-deep), var(--plum) 50%, var(--plum-deep));
    box-shadow: 0 3px 8px rgba(60,10,40,0.35);
  }
  .brand-name {
    position: absolute;
    left: 0;
    top: 266px;
    width: 600px;
    text-align: center;
    font-family: "Great Vibes", cursive;
    font-size: 84px;
    font-weight: 400;
    line-height: 1;
    color: var(--gold);
  }
  .brand-sub {
    position: absolute;
    left: 380px;
    top: 340px;
    font-family: "Great Vibes", cursive;
    font-size: 24px;
    line-height: 1;
    color: var(--gold);
  }
  .package-title {
    position: absolute;
    top: 388px;
    left: 0;
    width: 600px;
    text-align: center;
    font-family: "Cormorant SC", serif;
    font-weight: 700;
    font-size: 30px;
    letter-spacing: 1px;
    color: var(--plum-deep);
  }
  .package-list {
    position: absolute;
    top: 434px;
    left: 0;
    width: 600px;
    list-style: none;
    text-align: center;
    font-family: "Cinzel", serif;
    font-weight: 700;
    font-size: 13.5px;
    line-height: 17px;
    color: var(--plum);
  }
  .contact-band {
    position: absolute;
    left: 0;
    top: 660px;
    width: 600px;
    height: 180px;
  }
  .contact {
    position: absolute;
    left: 0;
    top: 710px;
    width: 600px;
    font-family: "Cormorant SC", serif;
    font-weight: 700;
    color: var(--gold);
  }
  .contact-title {
    text-align: center;
    font-size: 22px;
    margin-bottom: 10px;
  }
  .contact-row {
    display: flex;
    justify-content: space-between;
    padding: 0 50px;
    font-family: "Cinzel", serif;
    font-size: 18px;
  }
  .contact-item { display: flex; align-items: center; gap: 8px; }
  .contact-item svg { flex: none; }
</style>
</head>
<body>
  <main class="flyer">
    <div class="photo-frame">
      <div class="couple-photo" role="img" aria-label="Photograph of a bride and groom posing together"></div>
    </div>

    <div class="cake-art" role="img" aria-label="Illustration of a tiered wedding cake with red roses"></div>

    <p class="tagline">We will make<br>your special day<br>unforgettable</p>

    <p class="services-note">We can also decorate kids’ birthdays, sweet seventeens, baby and bridal showers and more.</p>

    <div class="brand-plaque"></div>
    <h1 class="brand-name">Evermore</h1>
    <p class="brand-sub">Decoration</p>

    <h2 class="package-title">Wedding Package</h2>
    <ul class="package-list">
      <li>Standard stage decoration (artificial)</li>
      <li>Welcome board / gate (gapura) – 1 pc</li>
      <li>Bridal room preparation suite (artificial) – 1 pc</li>
      <li>Aisle flowers – bunga jalan (artificial)</li>
      <li>Wedding car decoration (artificial) – 1 pc</li>
      <li>Hand bouquet for the bride (fresh) – 1 pc</li>
      <li>Flower petals – 1 pc</li>
      <li>Corsages for the groom and family (fresh) – 20 pcs</li>
      <li>Chair ribbons for the VIP table – 20 pcs</li>
      <li>Red cloth (kain merah) – 1 pc</li>
      <li>Wedding memory books, spiral bound – 4 pcs</li>
      <li>Angpau box</li>
    </ul>

    <svg class="contact-band" viewBox="0 0 600 180" preserveAspectRatio="none" aria-hidden="true">
      <defs>
        <linearGradient id="bandFill" x1="0" y1="0" x2="0" y2="1">
          <stop offset="0" stop-color="#7a2c62"/>
          <stop offset="1" stop-color="#4a1239"/>
        </linearGradient>
      </defs>
      <polygon fill="url(#bandFill)" points="0,30 30,22 55,34 90,14 120,28 160,18 200,36 240,20 275,30 310,12 350,28 390,18 430,34 470,16 505,30 540,20 575,32 600,22 600,180 0,180"/>
    </svg>

    <section class="contact">
      <p class="contact-title">Contact information</p>
      <div class="contact-row">
        <span class="contact-item">
          <svg width="20" height="18" viewBox="0 0 20 18" aria-hidden="true"><path d="M10 17 L2 9 A4.5 4.5 0 0 1 10 3 A4.5 4.5 0 0 1 18 9 Z" fill="#e8c04a"/></svg>
          +62800123456
        </span>
        <span class="contact-item">
          <svg width="24" height="16" viewBox="0 0 24 16" aria-hidden="true"><rect x="1" y="1" width="22" height="14" fill="none" stroke="#e8c04a" stroke-width="2"/><path d="M1 1 L12 9 L23 1" fill="none" stroke="#e8c04a" stroke-width="2"/></svg>
          clara.events@example.com
        </span>
      </div>
    </section>
  </main>
</body>
</html>
```